Meadowlark Counseling Business Card Design Project

I am starting a new business that provides counseling and coaching services to individuals and couples. These individuals are people looking to "transform" or grow in the personal lives. The design should convey trust, intimacy, hope, growth. It should be professional, elegant.
Contact information
Name: Dana R. Whitcombe
Title: Counselor and Life Coach
Slogan: Bringing Hope. Transforming Lives.
address: 47310 County Road 9, Suite 410
Plymouth, MN 55490
Phone: 763-555-0184
Email: dana@meadowlark-cx.example
website: www.meadowlark-cx.example
Back side of card should have bullets:
Individual counseling
Relationship counseling
Life Coaching for Teens and Adults
Group Workshops

```html
<!DOCTYPE html>
<html lang="en">
<head>
<meta charset="utf-8">
<title>Meadowlark Counseling – Business Card</title>
<link rel="stylesheet" href="https://fonts.googleapis.com/css2?family=Cinzel:wght@400&family=EB+Garamond:ital,wght@0,400;1,400&display=swap">
<style>
  :root {
    --page-bg: #e9ebee;
    --card-white: #ffffff;
    --deep-blue: #05365a;
    --ocean-blue: #0f74a3;
    --brand-blue: #1a6fa6;
    --accent-blue: #2a9fd0;
    --ink: #3a3f45;
    --silver: #dfe7ee;
    --rule: #9fb2c2;
  }
  * { box-sizing: border-box; margin: 0; padding: 0; }
  html, body {
    width: 1200px;
    height: 900px;
    overflow: hidden;
    background: var(--page-bg);
  }
  .sheet {
    width: 1200px;
    height: 900px;
    display: flex;
    flex-direction: column;
    align-items: center;
    justify-content: center;
    gap: 50px;
  }
  .card {
    position: relative;
    width: 640px;
    height: 366px;
    overflow: hidden;
    box-shadow: 0 6px 18px rgba(0, 0, 0, 0.18);
  }

  /* Back side */
  .card-back {
    background: radial-gradient(ellipse at 40% 45%, var(--ocean-blue) 0%, #0a5a84 45%, var(--deep-blue) 100%);
  }
  .card-back .halo {
    position: absolute;
    right: -40px;
    top: 40px;
    width: 300px;
    height: 300px;
    border-radius: 50%;
    background: rgba(255, 255, 255, 0.06);
  }
  .card-back .brand {
    position: absolute;
    left: 90px;
    top: 92px;
    display: flex;
    align-items: center;
    gap: 16px;
  }
  .card-back .brand-dot {
    width: 44px;
    height: 44px;
    border-radius: 50%;
    background: var(--silver);
  }
  .card-back .brand-name {
    font-family: "Cinzel", serif;
    font-size: 30px;
    letter-spacing: 1px;
    color: var(--silver);
  }
  .card-back .brand-rule {
    position: absolute;
    left: 150px;
    top: 146px;
    width: 350px;
    height: 1px;
    background: rgba(223, 231, 238, 0.6);
  }
  .card-back .slogan {
    position: absolute;
    left: 150px;
    top: 156px;
    width: 350px;
    font-family: "EB Garamond", serif;
    font-style: italic;
    font-size: 17px;
    letter-spacing: 0.5px;
    color: var(--silver);
  }
  .card-back .services {
    position: absolute;
    left: 150px;
    top: 208px;
    width: 380px;
    list-style: none;
    font-family: "EB Garamond", serif;
    font-size: 16px;
    line-height: 1.6;
    color: var(--silver);
  }
  .card-back .services li::before {
    content: "";
    display: inline-block;
    width: 6px;
    height: 6px;
    margin: 0 12px 2px 0;
    border-radius: 50%;
    background: var(--accent-blue);
  }

  /* Front side */
  .card-front { background: var(--card-white); }
  .card-front .brand-name {
    position: absolute;
    left: 40px;
    top: 34px;
    font-family: "Cinzel", serif;
    font-size: 38px;
    letter-spacing: 1px;
    color: var(--brand-blue);
  }
  .card-front .brand-rule {
    position: absolute;
    left: 40px;
    top: 92px;
    width: 560px;
    height: 1px;
    background: var(--rule);
  }
  .contact {
    position: absolute;
    left: 44px;
    top: 118px;
    font-family: "EB Garamond", serif;
    color: var(--ink);
    font-size: 15px;
    line-height: 1.45;
  }
  .contact .person {
    font-family: "Cinzel", serif;
    font-size: 21px;
    color: var(--accent-blue);
    letter-spacing: 0.5px;
    line-height: 1.1;
  }
  .contact .role { font-size: 13px; margin-bottom: 8px; }
  .contact .label { color: var(--accent-blue); margin-right: 4px; }
  .contact .web { color: var(--accent-blue); }
  .card-front .brand-dot {
    position: absolute;
    right: 70px;
    bottom: 50px;
    width: 110px;
    height: 110px;
    border-radius: 50%;
    background: radial-gradient(circle at 40% 35%, var(--accent-blue), var(--brand-blue));
  }
</style>
</head>
<body>
  <main class="sheet">
    <section class="card card-back" aria-label="Card back">
      <div class="halo"></div>
      <div class="brand">
        <div class="brand-dot"></div>
        <div class="brand-name">Meadowlark Counseling</div>
      </div>
      <div class="brand-rule"></div>
      <p class="slogan">Bringing Hope. Transforming Lives.</p>
      <ul class="services">
        <li>Individual counseling</li>
        <li>Relationship counseling</li>
        <li>Life Coaching for Teens and Adults</li>
        <li>Group Workshops</li>
      </ul>
    </section>

    <section class="card card-front" aria-label="Card front">
      <div class="brand-name">Meadowlark Counseling</div>
      <div class="brand-rule"></div>
      <div class="contact">
        <div class="person">Dana R. Whitcombe</div>
        <div class="role">Counselor and Life Coach</div>
        <div><span class="label">Phone</span>763-555-0184</div>
        <div><span class="label">Email</span>dana@meadowlark-cx.example</div>
        <div>47310 County Road 9, Suite 410 Plymouth, MN 55490</div>
        <div class="web">www.meadowlark-cx.example</div>
      </div>
      <div class="brand-dot"></div>
    </section>
  </main>
</body>
</html>
```